vault key finders.com

we are a new company that offer people that have lost there bit coin transaction a recovery and retrieval service
We are looking for a website that will allow you to fill in your details

name
email
bitcoins or other crypto lost and date of transaction

and then an auto reply to them from a given email to verify there email

I am looking for an easy for the client to leave there interest and has a security look around it and looks familiar to the user.

https://purserestore.example/?ref=Xq7LmT2vNp9RsK4wYb8ZcD1fGh6JkM3nQe5UtV0aBy

https://pursemendingaid.example

https://www.zennoro.example/faq-items/restoring-your-token-purse/

Target Market(s)

early investors into crypto

Industry/Entity Type

It Company

Logo Text

VAULTKEY FINDERS/LOCATORS

Coding

Coded - Design and coding required

Number of Pages Required

3 page

Requirements
Must have
• be able to :
• complete
• Name,
• Email
• transaction date of exchange and how much they invested

```html
<!DOCTYPE html>
<html lang="en">
<head>
<meta charset="utf-8">
<title>VaultKey Finders – Recovering Your Bitcoin Wallet</title>
<link rel="stylesheet" href="https://fonts.googleapis.com/css2?family=Open+Sans:ital,wght@0,400;0,600;0,700;0,800;1,600&display=swap">
<style>
:root{
  --gold:#d6b23a;
  --gold-deep:#b8922a;
  --gold-soft:#e7cf74;
  --ink:#1c1c1c;
  --text:#4a4a4a;
  --dark:#14161a;
  --dark-2:#23262b;
  --white:#ffffff;
  --field:#f1f1f1;
  --line:#d9d9d9;
}
*{box-sizing:border-box;margin:0;padding:0}
html,body{width:1200px;height:4119px;overflow:hidden}
body{position:relative;background:var(--white);font-family:"Open Sans",Arial,sans-serif;color:var(--text)}
.abs{position:absolute}

/* top bar + nav */
.topbar{left:0;top:0;width:1200px;height:27px;background:var(--gold);display:flex;justify-content:flex-end;align-items:center;gap:18px;padding-right:28px;font-size:12px;font-weight:600;color:var(--white)}
.topbar .item{display:flex;align-items:center;gap:6px}
.topbar .socials{display:flex;gap:4px}
.dot-social{width:18px;height:18px;border-radius:50%;border:1.5px solid var(--white)}
.navbar{left:0;top:27px;width:1200px;height:97px;background:var(--white)}
.brand{display:flex;align-items:center;gap:10px;white-space:nowrap}
.brand-mark{width:64px;height:64px;border-radius:50%;background:var(--ink);flex:0 0 auto}
.brand-name{font-size:30px;font-weight:700;color:var(--ink);letter-spacing:.5px}
.navbar .brand{position:absolute;left:38px;top:16px}
.menu{position:absolute;right:32px;top:32px;display:flex;gap:4px;font-size:14px;font-weight:700;color:var(--ink)}
.menu a{padding:6px 10px;text-decoration:none;color:inherit}
.menu a.active{border:1.5px solid var(--gold);color:var(--gold)}

/* hero */
.hero{left:0;top:124px;width:1200px;height:590px;background:radial-gradient(ellipse at 62% 45%,#8a6a1c 0%,#4a3810 35%,#161208 70%,#0b0a06 100%);clip-path:polygon(0 0,100% 0,100% 94%,50% 100%,0 94%)}
.hero h1{position:absolute;left:0;width:1200px;top:228px;text-align:center;font-size:48px;font-weight:800;color:var(--white);letter-spacing:1px}
.btn-gold{position:absolute;left:447px;top:320px;width:290px;height:50px;background:var(--gold);border:2px solid var(--gold-soft);color:var(--white);font-size:22px;font-weight:700;display:flex;align-items:center;justify-content:center;border-radius:3px}

/* section heading */
.sec-head{display:flex;align-items:center;gap:14px}
.sec-head .ring{width:62px;height:62px;border-radius:50%;border:3px solid var(--ink);background:var(--white)}
.sec-head h2{font-size:24px;font-weight:700;color:var(--ink);text-transform:uppercase}
.sec-head h2 span{color:var(--gold)}
.sec-head .rule{height:2px;width:90px;background:var(--gold)}

/* about */
.about-head{left:90px;top:820px}
.about-copy{left:77px;top:915px;width:612px;font-size:14px;line-height:23px;color:var(--text)}
.btn-dark{left:78px;top:1106px;display:flex;align-items:center}
.btn-dark .puck{width:52px;height:52px;border-radius:50%;background:var(--gold);border:4px solid var(--dark);z-index:1}
.btn-dark .bar{margin-left:-20px;width:230px;height:38px;background:var(--dark);color:var(--white);font-size:15px;font-weight:700;display:flex;align-items:center;justify-content:center;border-radius:0 4px 4px 0}

/* form */
.form-card{left:728px;top:815px;width:398px;height:448px;background:var(--white);box-shadow:0 4px 16px rgba(0,0,0,.25)}
.form-card .head{height:52px;background:var(--gold);color:var(--ink);font-size:17px;font-weight:800;display:flex;align-items:center;justify-content:center}
.form-body{padding:14px 22px 0 22px;display:flex;flex-direction:column;gap:10px}
.field{height:34px;background:var(--field);border:1px solid var(--line);font-size:12.5px;font-weight:700;color:var(--ink);padding:0 10px;display:flex;align-items:center;justify-content:space-between}
.field b{color:#c0392b}
.row{display:flex;gap:10px}
.row .field{flex:1}
.field.tall{height:84px;align-items:flex-start;padding-top:8px}
.submit{width:136px;height:32px;background:var(--dark);color:var(--white);font-size:14px;font-weight:700;display:flex;align-items:center;justify-content:center}

/* faq */
.faq{left:0;top:1345px;width:1200px;height:1050px;background:radial-gradient(ellipse at 30% 50%,#3a3f46 0%,#1e2126 45%,#0f1114 100%)}
.notch{left:0;width:1200px}
.faq-head{left:0;width:1200px;top:1512px;justify-content:center}
.faq-head h2{color:var(--gold)}
.faq-head h2 span{color:var(--white)}
.faq-list{left:316px;top:1606px;width:576px;display:flex;flex-direction:column;gap:10px}
.faq-item{background:var(--white);border-radius:8px;padding:0 14px;min-height:36px;font-size:14px;font-weight:700;color:var(--ink)}
.faq-item .q{height:36px;display:flex;align-items:center;justify-content:space-between}
.faq-item .a{font-size:13.5px;font-weight:400;line-height:21px;color:var(--text);padding-bottom:12px}
.faq-item.open{border:2px solid var(--gold)}

/* testimonials */
.testi-head{left:0;width:1200px;top:2455px;justify-content:center}
.quote-card{width:324px;height:144px;background:#ececec;padding:14px 16px;font-size:14px;line-height:20px;color:var(--ink);overflow:hidden}
.quote-card .mark{font-size:40px;font-weight:800;color:#777;line-height:20px;float:left;margin-right:6px}
.person{display:flex;align-items:center;justify-content:space-between;width:324px}
.person .name{font-size:15px;font-style:italic;font-weight:600;color:var(--ink)}
.avatar{width:84px;height:84px;border-radius:50%;border:4px solid var(--gold);background:linear-gradient(160deg,#d8c3a6,#8a7560)}

/* articles */
.articles{left:0;top:2856px;width:1200px;height:906px;background:linear-gradient(180deg,#1a1a18 0%,#4a3c18 45%,#8c7028 100%);clip-path:polygon(0 0,50% 3.5%,100% 0,100% 100%,0 100%)}
.art-head{left:0;width:1200px;top:3018px;justify-content:center}
.art-head h2{color:var(--gold)}
.art-head .ring{border-color:var(--gold);background:transparent}
.card{background:var(--white);overflow:hidden}
.card .photo{position:relative;width:100%}
.card .tag{position:absolute;left:-10px;top:-10px;width:108px;height:108px;border-radius:50%;background:rgba(214,178,58,.85);border:3px solid var(--white);color:var(--white);font-size:13px;font-weight:700;line-height:16px;display:flex;align-items:center;justify-content:center;text-align:center;padding:12px}
.card p{font-size:13.5px;line-height:20px;color:var(--ink);padding:10px 14px}
.view-all{left:494px;top:3620px;display:flex;align-items:center}
.view-all .puck{width:48px;height:48px;border-radius:50%;background:var(--gold);border:4px solid var(--dark);z-index:1}
.view-all .bar{margin-left:-18px;width:186px;height:38px;background:var(--dark);border:2px solid var(--white);color:var(--white);font-size:15px;font-weight:700;display:flex;align-items:center;justify-content:center;border-radius:0 19px 19px 0}

/* footer */
.footer{left:0;top:3762px;width:1200px;height:302px;background:var(--gold)}
.footer .brand{position:absolute;left:124px;top:108px;gap:8px}
.footer .brand-mark{width:44px;height:44px}
.footer .brand-name{font-size:22px;letter-spacing:0}
.foot-col{position:absolute;top:62px;font-size:13px;color:var(--ink)}
.foot-col h4{font-size:15px;font-weight:800;margin-bottom:6px;padding-bottom:4px;border-bottom:1.5px solid var(--ink);width:130px}
.foot-col.contact h4{width:200px}
.foot-col li{list-style:none;line-height:20px;font-weight:600}
.foot-line{display:flex;gap:8px;align-items:flex-start;margin-top:8px;line-height:17px;font-weight:600}
.foot-line .ic{flex:0 0 20px;height:20px;border-radius:50%;border:1.5px solid var(--ink)}
.request{position:absolute;left:865px;top:55px;width:233px;height:152px;background:var(--dark);border:3px solid var(--white);padding:14px;display:flex;flex-direction:column;align-items:center;gap:12px}
.request .btn{background:var(--gold);color:var(--ink);font-size:15px;font-weight:800;padding:8px 12px}
.request .small{color:var(--gold);font-size:12px;font-weight:700}
.request .socials{display:flex;gap:6px}
.request .socials span{width:22px;height:22px;border-radius:50%;border:1.5px solid var(--gold)}
.copyright{left:0;top:4064px;width:1200px;height:55px;background:var(--white);display:flex;align-items:center;justify-content:center;font-size:12px;font-weight:700;color:var(--ink)}
</style>
</head>
<body>

<header>
  <div class="abs topbar">
    <span class="item"><svg width="14" height="14" viewBox="0 0 24 24"><path fill="#fff" d="M6.6 10.8a15 15 0 0 0 6.6 6.6l2.2-2.2c.3-.3.7-.4 1-.2 1.1.4 2.3.6 3.6.6.6 0 1 .4 1 1V20c0 .6-.4 1-1 1A17 17 0 0 1 3 4c0-.6.4-1 1-1h3.5c.6 0 1 .4 1 1 0 1.3.2 2.5.6 3.6.1.3 0 .7-.2 1z"/></svg>(555) 014-2290</span>
    <span class="item"><svg width="14" height="14" viewBox="0 0 24 24"><path fill="none" stroke="#fff" stroke-width="2" d="M3 5h18v14H3zM3 5l9 8 9-8"/></svg>info@vaultkeyfinders.com</span>
    <span class="socials"><span class="dot-social"></span><span class="dot-social"></span><span class="dot-social"></span></span>
  </div>
  <nav class="abs navbar">
    <div class="brand"><span class="brand-mark"></span><span class="brand-name">VAULTKEY FINDERS</span></div>
    <div class="menu"><a class="active">HOME</a><a>ABOUT</a><a>FAQS</a><a>TESTIMONIALS</a><a>ARTICLES</a><a>CONTACT</a></div>
  </nav>
</header>

<section class="abs hero" role="img" aria-label="Glowing golden network globe of connected points over a dark background">
  <h1>RECOVERING YOUR BITCOIN WALLET</h1>
  <div class="btn-gold">GET STARTED</div>
</section>

<section class="about">
  <div class="abs sec-head about-head"><span class="ring"></span><h2>About VaultKey <span>Finders</span></h2></div>
  <p class="abs about-copy">Lorem ipsum dolor sit amet, consectetuer adipiscing elit, sed diam nonummy nibh euismod tincidunt ut laoreet dolore magna aliquam erat volutpat. Ut wisi enim ad minim veniam, quis nostrud exerci tation ullamcorper suscipit lobortis nisl ut aliquip ex ea commodo consequat. Duis autem vel eum iriure dolor in hendrerit in vulputate velit esse molestie consequat, vel illum dolore eu feugiat nulla facilisis at vero eros et accumsan et iusto odio dignissim qui blandit praesent luptatum zzril delenit augue duis dolore te feugait nulla facilisi.</p>
  <div class="abs btn-dark"><span class="puck"></span><span class="bar">Learn More</span></div>

  <form class="abs form-card">
    <div class="head">RECOVER YOUR WALLET NOW!</div>
    <div class="form-body">
      <div class="field"><span>Your Name<b>*</b></span></div>
      <div class="row"><div class="field"><span>Email Address<b>*</b></span></div><div class="field"><span>Phone Number</span></div></div>
      <div class="field"><span>Transaction Date<b>*</b></span><svg width="16" height="16" viewBox="0 0 24 24"><path fill="none" stroke="#1c1c1c" stroke-width="2" d="M4 6h16v14H4zM4 10h16M8 3v5M16 3v5"/></svg></div>
      <div class="field"><span>Amount Invested<b>*</b></span><svg width="12" height="8" viewBox="0 0 12 8"><path fill="#1c1c1c" d="M0 0h12L6 8z"/></svg></div>
      <div class="field"><span>What Wallet Did You Use to Store Your Coins?</span></div>
      <div class="field tall"><span>What Problem Are You Having With Your Wallet?</span></div>
      <div class="submit">SUBMIT</div>
    </div>
  </form>
</section>

<section class="abs faq" role="img" aria-label="Dark photo of a hand touching a digital coin interface"></section>
<svg class="abs notch" style="top:1345px" width="1200" height="60" viewBox="0 0 1200 60"><polygon points="0,0 1200,0 1200,20 600,55 0,20" fill="#fff"/></svg>
<svg class="abs notch" style="top:2335px" width="1200" height="60" viewBox="0 0 1200 60"><polygon points="0,60 0,5 600,40 1200,5 1200,60" fill="#fff"/></svg>
<div class="abs sec-head faq-head"><span class="rule"></span><span style="width:22px;height:22px;border-radius:50%;border:2px solid var(--gold)"></span><h2>Frequently Asked <span>Questions</span></h2><span class="rule"></span></div>
<div class="abs faq-list">
  <div class="faq-item"><div class="q">Can you recover my wallet?<svg width="12" height="8" viewBox="0 0 12 8"><path fill="none" stroke="#1c1c1c" stroke-width="2" d="M1 1l5 5 5-5"/></svg></div></div>
  <div class="faq-item open"><div class="q">Which currencies/wallets can you recover?<svg width="12" height="8" viewBox="0 0 12 8"><path fill="none" stroke="#1c1c1c" stroke-width="2" d="M1 7l5-5 5 5"/></svg></div>
    <div class="a">Lorem ipsum dolor sit amet, consectetuer adipiscing elit, sed diam nonummy nibh euismod tincidunt ut laoreet dolore magna aliquam erat volutpat. Ut wisi enim ad minim veniam, quis nostrud exerci tation ullamcorper suscipit lobortis nisl ut aliquip ex ea commodo consequat. Duis autem vel eum iriure dolor in hendrerit in vulputate velit esse molestie consequat, vel illum dolore eu feugiat nulla facilisis at vero eros et accumsan et iusto odio dignissim qui blandit praesent luptatum zzril delenit augue.</div></div>
  <div class="faq-item"><div class="q">Why should I trust you?<svg width="12" height="8" viewBox="0 0 12 8"><path fill="none" stroke="#1c1c1c" stroke-width="2" d="M1 1l5 5 5-5"/></svg></div></div>
  <div class="faq-item"><div class="q">Will you keep my coins safe and my information confidential?<svg width="12" height="8" viewBox="0 0 12 8"><path fill="none" stroke="#1c1c1c" stroke-width="2" d="M1 1l5 5 5-5"/></svg></div></div>
  <div class="faq-item"><div class="q">How are you different from other wallet recovery services?<svg width="12" height="8" viewBox="0 0 12 8"><path fill="none" stroke="#1c1c1c" stroke-width="2" d="M1 1l5 5 5-5"/></svg></div></div>
  <div class="faq-item"><div class="q">What happens after you recover my wallet?<svg width="12" height="8" viewBox="0 0 12 8"><path fill="none" stroke="#1c1c1c" stroke-width="2" d="M1 1l5 5 5-5"/></svg></div></div>
  <div class="faq-item"><div class="q">I can't login to my LedgerVista wallet. Can you help?<svg width="12" height="8" viewBox="0 0 12 8"><path fill="none" stroke="#1c1c1c" stroke-width="2" d="M1 1l5 5 5-5"/></svg></div></div>
  <div class="faq-item"><div class="q">I need help buying/selling/trading Bitcoin. Can you help?<svg width="12" height="8" viewBox="0 0 12 8"><path fill="none" stroke="#1c1c1c" stroke-width="2" d="M1 1l5 5 5-5"/></svg></div></div>
  <div class="faq-item"><div class="q">Can you help me with CoinHarbor, PayMint, Tidewell, or another exchange?<svg width="12" height="8" viewBox="0 0 12 8"><path fill="none" stroke="#1c1c1c" stroke-width="2" d="M1 1l5 5 5-5"/></svg></div></div>
  <div class="faq-item"><div class="q">How can I contact you securely?<svg width="12" height="8" viewBox="0 0 12 8"><path fill="none" stroke="#1c1c1c" stroke-width="2" d="M1 1l5 5 5-5"/></svg></div></div>
</div>

<section class="testimonials">
  <div class="abs sec-head testi-head"><span class="rule"></span><span class="ring"></span><h2>Testimonials</h2><span class="rule"></span></div>
  <div class="abs quote-card" style="left:88px;top:2560px"><span class="mark">“</span>Lorem ipsum dolor sit amet, consectetuer adipiscing elit, sed diam nonummy nibh euismod tincidunt ut laoreet dolore magna aliquam erat volutpat. <b>”</b></div>
  <div class="abs quote-card" style="left:440px;top:2560px"><span class="mark">“</span>Lorem ipsum dolor sit amet, consectetuer adipiscing elit, sed diam nonummy nibh euismod tincidunt ut laoreet dolore magna aliquam erat volutpat. <b>”</b></div>
  <div class="abs quote-card" style="left:790px;top:2560px"><span class="mark">“</span>Lorem ipsum dolor sit amet, consectetuer adipiscing elit, sed diam nonummy nibh euismod tincidunt ut laoreet dolore magna aliquam erat volutpat. <b>”</b></div>
  <div class="abs person" style="left:88px;top:2714px"><span class="name">Maren Holloway</span><span class="avatar" role="img" aria-label="Portrait photo of a client"></span></div>
  <div class="abs person" style="left:440px;top:2714px"><span class="name">Priya Castell</span><span class="avatar" role="img" aria-label="Portrait photo of a client"></span></div>
  <div class="abs person" style="left:790px;top:2714px"><span class="name">Declan Ashford</span><span class="avatar" role="img" aria-label="Portrait photo of a client"></span></div>
</section>

<section class="abs articles" role="img" aria-label="Blurred golden photo of a payment card and cash"></section>
<div class="abs sec-head art-head"><span class="rule"></span><span class="ring"></span><h2>Articles</h2><span class="rule"></span></div>
<article class="abs card" style="left:96px;top:3130px;width:316px;height:440px">
  <div class="photo" style="height:192px;background:linear-gradient(135deg,#dfe6ec,#8fa3b5)" role="img" aria-label="Office photo of a team meeting around a laptop"><span class="tag" style="left:0;top:0">How to Become a Powerful Investor</span></div>
  <p>Lorem ipsum dolor sit amet, consectetuer adipiscing elit, sed diam nonummy nibh euismod tincidunt ut laoreet dolore magna aliquam erat volutpat. Ut wisi enim ad minim veniam, quis nostrud exerci tation ullamcorper suscipit lobortis nisl ut aliquip ex ea commodo consequat. Duis autem vel eum iriure dolor in hendrerit in vulputate velit esse molestie consequat, vel illum dolore eu feugiat nulla facilisis at vero eros et accumsan et.</p>
</article>
<article class="abs card" style="left:448px;top:3130px;width:315px;height:206px">
  <div class="photo" style="height:128px;background:linear-gradient(135deg,#cfdde8,#6f8ea8)" role="img" aria-label="Photo of a person leaping over a city skyline"><span class="tag" style="left:0;top:0">Become an Inspiration and Rule The World</span></div>
  <p>Lorem ipsum dolor sit amet, consectetuer adipiscing elit, sed diam nonummy nibh euismod.</p>
</article>
<article class="abs card" style="left:790px;top:3130px;width:336px;height:206px">
  <div class="photo" style="height:128px;background:linear-gradient(135deg,#b9c3cc,#4f5f70)" role="img" aria-label="Photo of business people reviewing documents"><span class="tag" style="left:0;top:0">Be the Leader You Wish</span></div>
  <p>Lorem ipsum dolor sit amet, consectetuer adipiscing elit, sed diam nonummy nibh euismod.</p>
</article>
<article class="abs card" style="left:448px;top:3364px;width:315px;height:206px">
  <div class="photo" style="height:128px;background:linear-gradient(135deg,#eef0f2,#a4aeb8)" role="img" aria-label="Photo of a hand on a tablet with charts"><span class="tag" style="left:0;top:0">Overcome Your Fear</span></div>
  <p>Lorem ipsum dolor sit amet, consectetuer adipiscing elit, sed diam nonummy nibh euismod.</p>
</article>
<article class="abs card" style="left:790px;top:3364px;width:336px;height:206px">
  <div class="photo" style="height:128px;background:linear-gradient(135deg,#c8d2dc,#5a6c7e)" role="img" aria-label="Photo of a businessman using a smartphone"><span class="tag" style="left:0;top:0">Become a Successful Entrepreneur</span></div>
  <p>Lorem ipsum dolor sit amet, consectetuer adipiscing elit, sed diam nonummy nibh euismod.</p>
</article>
<div class="abs view-all"><span class="puck"></span><span class="bar">View All</span></div>

<footer class="abs footer">
  <div class="brand"><span class="brand-mark"></span><span class="brand-name">VAULTKEY FINDERS</span></div>
  <div class="foot-col" style="left:448px"><h4>QUICK LINKS</h4><ul><li>Home</li><li>About</li><li>FAQS</li><li>Testimonials</li><li>Articles</li><li>Contact</li></ul></div>
  <div class="foot-col contact" style="left:610px"><h4>CONTACT</h4>
    <div class="foot-line"><span class="ic"></span><span>VAULTKEY FINDERS<br>27 Harrowgate Lane<br>LEEDS, ENGLAND 00000</span></div>
    <div class="foot-line"><span class="ic"></span><span>(555) 014-2290</span></div>
    <div class="foot-line"><span class="ic"></span><span>info@vaultkeyfinders.com</span></div>
  </div>
  <div class="request"><span class="btn">REQUEST MORE INFO</span><span class="small">CONNECT WITH US</span><span class="socials"><span></span><span></span><span></span></span></div>
</footer>
<div class="abs copyright">COPYRIGHT © 2018 VAULTKEY FINDERS ALL RIGHTS RESERVED.</div>

</body>
</html>
```